Stylish Business Cards Wanted

- DOUBLE SIDED Design Required -

High end, edgy cards for a corporate and personal stylist. Must include logo,
Name: Belinda Forsey
Title: Director and Stylist
telephone : +61 8 8217 4592
email: belinda@thegarbledger.example
website: thegarbledger.example
Tag: Corporate Workwear & Uniform Specialist | Personal Stylist
Would like nice icons for telephone, email, website

Target Market(s)

Businesses wanting stylish uniforms, people wanting stylish wardrobes

Industry/Entity Type

Corporate Workwear Stylist

Contact Information for Business Card

I would like black, white and gold foiling incorporated in the design - possibly a touch of the other colours on my branding guide attached Name: Belinda Forsey Title: Director and Stylist telephone : +61 8 8217 4592 email: belinda@thegarbledger.example website: thegarbledger.example Tag: Corporate Workwear & Uniform Specialist | Personal Stylist Would like nice icons for telephone, email, website

Font styles to use
Other font styles liked:
• Raleway

Colors

Designer to choose colors to be used in the design.

Requirements
Must have
• Gold foil accents

```html
<!DOCTYPE html>
<html lang="en">
<head>
<meta charset="utf-8">
<title>The Garb Ledger — Business Cards</title>
<link rel="stylesheet" href="https://fonts.googleapis.com/css2?family=Raleway:wght@400;500;600&display=swap">
<style>
  :root {
    --backdrop: #2b2b2d;
    --card: #1c1c1d;
    --white: #f2f2f2;
    --grey: #cfcfcf;
    --gold: #d9b445;
    --gold-light: #f4dc6a;
    --gold-deep: #a9801d;
  }
  * { box-sizing: border-box; margin: 0; padding: 0; }
  html, body {
    width: 1200px;
    height: 868px;
    overflow: hidden;
    background: var(--backdrop);
    font-family: "Raleway", sans-serif;
  }
  .sheet {
    position: relative;
    width: 1200px;
    height: 868px;
  }
  .card {
    position: absolute;
    top: 134px;
    width: 360px;
    height: 600px;
    background: var(--card);
    overflow: hidden;
    box-shadow: 0 18px 40px rgba(0,0,0,0.45);
  }
  .card--front { left: 150px; }
  .card--back { left: 690px; }

  /* Front */
  .lettering {
    position: absolute;
    top: 44px;
    left: 0;
    width: 300px;
    height: 300px;
    background: linear-gradient(135deg, var(--gold-light) 0%, var(--gold) 45%, var(--gold-deep) 100%);
    border-radius: 0 140px 40px 0;
  }
  .contact {
    position: absolute;
    left: 120px;
    right: 24px;
    top: 382px;
    text-align: center;
  }
  .contact__name {
    color: var(--white);
    font-size: 19px;
    font-weight: 500;
    letter-spacing: 1px;
    text-transform: uppercase;
  }
  .contact__title {
    color: var(--gold);
    font-size: 13px;
    margin-top: 4px;
  }
  .contact__rule {
    width: 34px;
    height: 1px;
    background: var(--grey);
    margin: 18px auto;
  }
  .contact__line {
    color: var(--grey);
    font-size: 11.5px;
    line-height: 1.55;
  }

  /* Back */
  .brand {
    position: absolute;
    top: 200px;
    left: 0;
    right: 0;
    display: flex;
    align-items: center;
    justify-content: center;
    gap: 12px;
  }
  .brand__square {
    width: 14px;
    height: 14px;
    background: var(--gold);
  }
  .brand__name {
    color: var(--white);
    font-size: 24px;
    font-weight: 600;
    letter-spacing: 3px;
    text-transform: uppercase;
  }
  .tagline {
    position: absolute;
    top: 380px;
    left: 0;
    right: 0;
    text-align: center;
    color: var(--grey);
    font-size: 11px;
    letter-spacing: 1px;
    line-height: 1.6;
    text-transform: uppercase;
  }
</style>
</head>
<body>
<main class="sheet">
  <section class="card card--front">
    <div class="lettering" role="img" aria-label="Large gold foil hand-lettered word in script"></div>
    <div class="contact">
      <p class="contact__name">Belinda Forsey</p>
      <p class="contact__title">Director &amp; Stylist</p>
      <div class="contact__rule"></div>
      <p class="contact__line">+61 8 8217 4592</p>
      <p class="contact__line">belinda@thegarbledger.example</p>
      <p class="contact__line">thegarbledger.example</p>
    </div>
  </section>

  <section class="card card--back">
    <div class="brand">
      <span class="brand__square"></span>
      <span class="brand__name">The Garb Ledger</span>
    </div>
    <p class="tagline">Corporate Workwear<br>Uniform Specialist<br>Personal Stylist</p>
  </section>
</main>
</body>
</html>
```